Quillmarsh Trades Landing Page

I need a landing page for a campaign advertising quillmarsh trades trading. The campaign and overall look and feel should be inspired by this brand: https://quillmarshtrades.com/

The screenshots you want to add from the trading area you can simple google. We will replace any screenshots with actual screenshots from our binary trading software.

You can also copy the text since we will replace the text as well.

The name to advertise is "Tandel Pilot - Harvest Methods" and will be featured on www.tandelpilot.ws

What is important is the overall look!
- Tandel Pilot
- Clean Design
- Nice colors
- Makes you want to signup and trade!

Target Market(s)

People who wants to earn some extra money by investing and trading options online.

Industry/Entity Type

Advertising

Logo Text

TAndelPilot - Harvest Method

Number of Pages Required

1 page

Colors

Designer to choose colors to be used in the design.

Requirements
Must have
• New Logo or remake of current logo
• Design for web resolution
• Design for mobile resolution
• Signup form as attached but designed more flashy!
• The chat popup may not block crucial elements of the design
Nice to have
• Screenshots that makes people interested to signup
• Catchy phrases that will get people interested in the product
• You are allowed to copy or partly copy the current logo
• Design a contact page
Should not have
• US flags

```html
<!DOCTYPE html>
<html lang="en">
<head>
<meta charset="utf-8">
<title>Quillmarsh Trades – Tandel Pilot</title>
<link href="https://fonts.googleapis.com/css2?family=Open+Sans:wght@400;600;700&family=Montserrat:wght@400;600;700&display=swap" rel="stylesheet">
<style>
:root{
  --ink:#2b2b2b;
  --muted:#555;
  --navy:#1c2b47;
  --navy-deep:#15203a;
  --nav-bg:#0c0f16;
  --sky:#5aa6de;
  --hero-a:#0b1d3a;
  --hero-b:#2f6fb3;
  --light:#efefef;
  --pattern:#e9e9e9;
  --green:#5cb85c;
  --orange:#f39c12;
  --gold:#e6b422;
  --line:#cfcfcf;
  --footer:#111;
  --footer-deep:#000;
  --white:#fff;
}
*{box-sizing:border-box;margin:0;padding:0}
html,body{width:1200px;height:4100px;overflow:hidden}
body{position:relative;font-family:"Open Sans",Arial,sans-serif;color:var(--ink);background:var(--white)}
.abs{position:absolute}
section,header,footer{position:absolute;left:0;width:1200px}

/* top bar + nav */
.topbar{top:0;height:38px;background:var(--nav-bg);color:#ccc;font-size:14px;border-bottom:1px solid #222}
.topbar .lang{left:60px;top:10px}
.topbar .login{left:935px;top:10px}
.topbar .open{left:1040px;top:10px}
.nav{top:38px;height:112px;background:var(--nav-bg)}
.brand{left:55px;top:30px;display:flex;align-items:center;gap:14px;color:var(--white)}
.brand-mark{width:46px;height:46px;border-radius:50%;background:var(--sky)}
.brand-name{font-family:"Montserrat",sans-serif;font-weight:700;font-size:24px;line-height:1.1}
.brand-name small{display:block;font-size:24px;font-weight:700}
.nav-links{top:44px;left:0;width:1200px;font-size:16px;color:var(--white)}
.nav-links span{position:absolute}

/* hero */
.hero{top:150px;height:457px}
.hero-visual{inset:0;background:linear-gradient(120deg,var(--hero-a) 0%,#163a6b 45%,var(--hero-b) 75%,#9bc3e6 100%)}
.signup{left:55px;top:36px;width:267px}
.field{position:absolute;left:0;width:267px;height:36px;background:var(--white);border-radius:3px;font-size:12px;color:#888;padding:10px 12px}
.captcha{position:absolute;left:0;top:268px;width:260px;height:64px;background:#f9f9f9;border:1px solid #d3d3d3;border-radius:3px;font-size:13px;color:#333}
.captcha i{position:absolute;left:14px;top:20px;width:24px;height:24px;border:2px solid #c1c1c1;background:var(--white);border-radius:2px}
.captcha span{position:absolute;left:50px;top:22px}
.captcha b{position:absolute;right:14px;top:14px;width:32px;height:32px;border-radius:50%;background:#4a90e2;opacity:.75}
.check{position:absolute;left:0;font-size:10px;color:var(--white);display:flex;gap:8px;align-items:center}
.check i{width:12px;height:12px;background:var(--white);display:inline-block}
.cta-open{position:absolute;left:0;top:388px;width:267px;height:42px;background:var(--sky);color:var(--white);font-size:15px;text-align:center;line-height:42px;border-radius:3px}
.award{left:960px;top:250px;width:155px;height:155px;border-radius:50%;background:radial-gradient(circle,#f7d24d 0%,var(--gold) 60%,#b98a10 100%)}
.pay-strip{left:951px;top:394px;width:189px;height:36px;background:var(--white);border-radius:2px}

/* steps */
.steps{top:607px;height:413px;background:var(--light)}
.title-caps{font-family:"Montserrat",sans-serif;font-size:34px;font-weight:400;letter-spacing:1px;text-align:center;width:1200px;color:#222}
.step-ico{width:174px;height:174px;border-radius:50%;background:var(--navy)}
.step-label{font-size:24px;color:#333;text-align:center;width:360px}

/* about */
.about{top:1020px;height:525px;background:var(--white)}
.h-big{font-family:"Montserrat",sans-serif;font-weight:700;font-size:40px;color:#222}
.about .sub{left:55px;top:140px;font-size:23px;color:#666}
.about p{position:absolute;left:55px;width:720px;font-size:19px;line-height:1.4;color:#333}
.btn-dark{left:55px;top:431px;width:218px;height:52px;background:var(--navy);color:var(--white);font-weight:700;font-size:19px;text-align:center;line-height:52px;border-radius:6px}
.about-visual{left:806px;top:114px;width:314px;height:396px;border-radius:40px;background:radial-gradient(ellipse at 50% 45%,#7fc3ee 0%,#d9e6ef 55%,var(--white) 80%)}

/* best */
.best{top:1545px;height:792px;background:var(--pattern)}
.center{text-align:center;width:1200px;left:0}
.best .intro{top:125px;left:110px;width:980px;font-size:18px;line-height:1.45;text-align:center;color:#444}
.col-h{font-weight:700;font-size:21px;color:#222}
.col-p{font-size:15.5px;line-height:1.4;color:#444;width:510px}
.tick{width:44px;height:44px;border-radius:50%;background:var(--green)}
.tick-label{font-weight:700;font-size:24px;color:#333;text-align:center;width:400px}

/* features */
.features{top:2337px;height:588px;background:var(--white)}
.features .h{top:45px;font-weight:700;font-size:24px}
.features .intro{top:88px;left:140px;width:920px;font-size:16px;line-height:1.45;text-align:center;color:#444}
.num{width:60px;height:60px;background:var(--navy);color:var(--white);font-weight:700;font-size:34px;text-align:center;line-height:60px}
.feat-h{font-weight:700;font-size:23px;color:#222}
.feat-p{font-size:16px;line-height:1.45;color:#444;width:400px}

/* dashboard */
.dash{top:2930px;height:350px;background:var(--white)}
.dash-frame{left:55px;top:0;width:1090px;height:350px;overflow:hidden}
.tab{position:absolute;top:3px;height:33px;font-size:12px;text-align:center;line-height:33px}
.dash-head{position:absolute;top:48px;left:0;width:1090px;font-size:14px;color:#333}
.dash-head span,.dash-row span{position:absolute}
.dash-row{position:absolute;top:90px;left:0;width:1090px;height:48px;font-size:15px;color:#333;border-bottom:1px solid #ddd}
.toggle{width:60px;height:22px;border-radius:3px;background:var(--sky)}
.dash-lower{position:absolute;left:0;top:142px;width:1090px;height:208px;background:linear-gradient(#f2f2f2,#fafafa 60%,var(--white))}
.dash-lower .label{position:absolute;font-size:17px;color:#333}
.opt{position:absolute;font-size:13px;color:#444}
.fade{position:absolute;left:0;bottom:0;width:1090px;height:110px;background:linear-gradient(rgba(255,255,255,0),var(--white))}

/* contact */
.contact{top:3280px;height:465px;background:var(--white)}
.contact .h{top:45px;font-family:"Montserrat",sans-serif;font-weight:700;font-size:24px}
.input{width:429px;height:42px;border:1px solid var(--line);font-size:13px;color:#777;padding:12px 12px}
.textarea{left:533px;top:125px;width:604px;height:197px;border:1px solid var(--line);font-size:13px;color:#777;padding:12px}
.btn-msg{left:525px;top:363px;width:131px;height:41px;border:1px solid var(--sky);color:var(--sky);font-size:15px;text-align:center;line-height:39px}

/* footer */
.footer{top:3745px;height:315px;background:var(--footer);color:var(--white)}
.footer h4{position:absolute;font-weight:700;font-size:20px}
.legal{left:55px;top:95px;width:560px;font-size:10.5px;line-height:1.55;color:#bbb}
.links{left:680px;top:92px;font-size:15px;line-height:36px}
.links li{list-style:none}
.links li::before{content:"›";margin-right:22px}
.social{top:88px;width:30px;height:30px;border-radius:50%}
.copy{top:4060px;height:40px;background:var(--footer-deep);color:#ccc;font-size:13px;text-align:center;line-height:40px}
</style>
</head>
<body>

<header class="topbar">
  <span class="abs lang">⊕ English ▾</span>
  <span class="abs login">⇥ Login</span>
  <span class="abs open">● Open Account</span>
</header>

<header class="nav">
  <div class="abs brand">
    <span class="brand-mark"></span>
    <div class="brand-name">Tandel Pilot<small>Harvest Methods</small></div>
  </div>
  <nav class="abs nav-links">
    <span style="left:682px">Home</span>
    <span style="left:785px">About</span>
    <span style="left:880px">FAQ</span>
    <span style="left:980px">Guides</span>
    <span style="left:1085px">Contact</span>
  </nav>
</header>

<section class="hero">
  <div class="abs hero-visual" role="img" aria-label="Photo of robot hands typing on a laptop in blue light"></div>
  <form class="abs signup">
    <div class="field" style="top:0">First Name</div>
    <div class="field" style="top:44px">Last Name</div>
    <div class="field" style="top:90px">Email</div>
    <div class="field" style="top:136px">Password</div>
    <div class="field" style="top:183px;width:55px">+1</div>
    <div class="field" style="top:183px;left:63px;width:204px">Phone number</div>
    <div class="captcha"><i></i><span>I'm not a robot</span><b></b></div>
    <div class="check" style="top:341px"><i></i>Yes, I would like to receive your newsletter</div>
    <div class="check" style="top:363px"><i></i>I accept terms &amp; conditions</div>
    <div class="cta-open">Open Free Account</div>
  </form>
  <div class="abs award" role="img" aria-label="Award badge"></div>
  <svg class="abs pay-strip" viewBox="0 0 189 36" aria-label="Payment methods">
    <rect x="8" y="10" width="30" height="16" fill="#1a3e8c"/>
    <rect x="46" y="10" width="30" height="16" fill="#f0a020"/>
    <rect x="84" y="10" width="30" height="16" fill="#2a7ad0"/>
    <rect x="122" y="10" width="26" height="16" fill="#d33"/>
    <rect x="156" y="10" width="24" height="16" fill="#777"/>
  </svg>
</section>

<section class="steps">
  <h2 class="abs title-caps" style="top:52px">GET STARTED IN 3 EASY STEPS</h2>
  <svg class="abs step-ico" style="left:143px;top:129px" viewBox="0 0 174 174" aria-label="Key icon">
    <circle cx="87" cy="87" r="87" fill="#1c2b47"/>
    <circle cx="70" cy="87" r="18" fill="none" stroke="#fff" stroke-width="8"/>
    <path d="M88 87h40M116 87v14M128 87v10" stroke="#fff" stroke-width="8" fill="none"/>
  </svg>
  <svg class="abs step-ico" style="left:473px;top:129px" viewBox="0 0 174 174" aria-label="Coin icon">
    <circle cx="87" cy="87" r="87" fill="#1c2b47"/>
    <circle cx="87" cy="87" r="44" fill="none" stroke="#fff" stroke-width="7"/>
    <text x="87" y="107" text-anchor="middle" font-family="Open Sans,sans-serif" font-weight="700" font-size="56" fill="#fff">$</text>
  </svg>
  <svg class="abs step-ico" style="left:873px;top:129px" viewBox="0 0 174 174" aria-label="Automation icon">
    <circle cx="87" cy="87" r="87" fill="#1c2b47"/>
    <rect x="60" y="52" width="54" height="44" rx="10" fill="#fff"/>
    <rect x="54" y="102" width="66" height="28" rx="6" fill="#fff"/>
    <rect x="84" y="38" width="6" height="14" fill="#fff"/>
  </svg>
  <p class="abs step-label" style="left:50px;top:332px">Open a free account</p>
  <p class="abs step-label" style="left:380px;top:332px">Deposit (no fees!)</p>
  <p class="abs step-label" style="left:780px;top:332px">Begin robot trading!</p>
</section>

<section class="about">
  <h2 class="abs h-big" style="left:55px;top:52px">About Quillmarsh Trades</h2>
  <p class="sub abs">Auto Trades by QuillmarshTrades.com</p>
  <p style="top:172px">Looking to have a trading experience that is both secure and simple? You finally can with the auto trading system provided by QuillmarshTrades.com. If you are someone who doesn't have enough time to trade yourself, then the auto trader is definitely the right choice for you.</p>
  <p style="top:300px">New in the trading world, our robot provides traders with updated signals and quickly executed trades that enables them to stay successful and gain profits. Operating on a mechanism that is both practical and highly technological, it is very easy to use.</p>
  <div class="abs btn-dark">Read More</div>
  <div class="abs about-visual" role="img" aria-label="Illustration of a friendly trading robot holding an envelope"></div>
</section>

<section class="best">
  <h2 class="abs h-big center" style="top:45px;font-size:38px">The Best Tandel Pilot</h2>
  <p class="abs intro">Quillmarsh Trades is a premium trading software that finds all the best opportunities from the market for you. Trade with the best brokers on the market, and benefit from this extraordinary trading experience.</p>
  <h3 class="abs col-h" style="left:55px;top:278px">Safe &amp; Secure - Automatic stop loss</h3>
  <p class="abs col-p" style="left:55px;top:312px">You do not have to worry about losing your funds. You set your own limits and decide how much you want to risk and trade per day. Other auto trading robots offer high rewards but empty the traders' accounts overnight and collaborate with the brokers by placing a series of losing trades.</p>
  <h3 class="abs col-h" style="left:630px;top:278px">No Downloads - No Charges</h3>
  <p class="abs col-p" style="left:630px;top:312px">You only have to set up your account once and increase your chances to make a profit. Don't waste time downloading and installing outdated software that needs regular updates. We handle everything on our revolutionary binary trading system.</p>
  <h3 class="abs col-h center" style="top:452px">Trusted Tandel Pilot</h3>
  <p class="abs center" style="top:488px;left:300px;width:600px;font-size:15.5px;line-height:1.45;color:#444">Our system is exceptionally user-friendly and allows you to place trades with an advantage! When your account is set up, you are good to go. Most binary trading robots are not as accommodating as our Robot is. So, begin your journey with Quillmarsh Trades!</p>
  <svg class="abs tick" style="left:197px;top:625px" viewBox="0 0 44 44" aria-label="Tick"><circle cx="22" cy="22" r="22" fill="#5cb85c"/><path d="M12 23l7 7 13-15" stroke="#fff" stroke-width="5" fill="none"/></svg>
  <svg class="abs tick" style="left:538px;top:625px" viewBox="0 0 44 44" aria-label="Tick"><circle cx="22" cy="22" r="22" fill="#5cb85c"/><path d="M12 23l7 7 13-15" stroke="#fff" stroke-width="5" fill="none"/></svg>
  <svg class="abs tick" style="left:970px;top:625px" viewBox="0 0 44 44" aria-label="Tick"><circle cx="22" cy="22" r="22" fill="#5cb85c"/><path d="M12 23l7 7 13-15" stroke="#fff" stroke-width="5" fill="none"/></svg>
  <p class="abs tick-label" style="left:19px;top:700px">Free Binary Trading Software</p>
  <p class="abs tick-label" style="left:360px;top:700px">No downloads required</p>
  <p class="abs tick-label" style="left:792px;top:700px">Multiple brokers available</p>
</section>

<section class="features">
  <h2 class="abs h center">Quillmarsh Trades</h2>
  <p class="abs intro">Many traders enjoy various benefits of Quillmarsh Trades that independently monitors the market and searches for trading opportunities with the subsequent execution of transactions. Let's look what we can offer as an automated trading system.</p>
  <svg class="abs" style="left:55px;top:175px" width="1093" height="415" aria-hidden="true">
    <line x1="549" y1="0" x2="549" y2="415" stroke="#cfcfcf" stroke-width="2"/>
    <line x1="0" y1="202" x2="1093" y2="202" stroke="#cfcfcf" stroke-width="2"/>
  </svg>
  <div class="abs num" style="left:55px;top:199px">1</div>
  <h3 class="abs feat-h" style="left:160px;top:199px">Safe &amp; Secure Trading</h3>
  <p class="abs feat-p" style="left:160px;top:238px">Algorithm Trading<br>The majority of traders' mistakes is linked to the fact that at a certain time there is a fear that following transactions can be unprofitable.</p>
  <div class="abs num" style="left:640px;top:199px">2</div>
  <h3 class="abs feat-h" style="left:745px;top:199px">Rationality</h3>
  <p class="abs feat-p" style="left:745px;top:238px">Unlike newbie traders whose speculations and conclusions on the background of the installed templates are subjective, Quillmarsh Trades has a maximum transparency</p>
  <div class="abs num" style="left:55px;top:418px">3</div>
  <h3 class="abs feat-h" style="left:160px;top:418px">Velocity</h3>
  <p class="abs feat-p" style="left:160px;top:457px">Since our sophisticated algorithms react instantly to current trends on financial markets, Quillmarsh Trades opens a position immediately as soon as the requirements of the trading plan is ex</p>
  <div class="abs num" style="left:640px;top:418px">4</div>
  <h3 class="abs feat-h" style="left:745px;top:418px">Diversification</h3>
  <p class="abs feat-p" style="left:745px;top:457px">Quillmarsh Trades allows you to trade different assets or different strategies at the same time. It allows you to spread risk across many trading instruments. If binary options trading seems difficult</p>
</section>

<section class="dash">
  <div class="abs dash-frame">
    <div class="tab" style="left:0;width:360px;background:#e6e6e6;color:#333">Robot Settings</div>
    <div class="tab" style="left:360px;width:365px;background:var(--navy-deep);color:#fff">History</div>
    <div class="tab" style="left:725px;width:365px;background:var(--navy-deep);color:#fff">Profile</div>
    <div class="dash-head">
      <span style="left:40px">Brokers</span><span style="left:200px">Balance</span><span style="left:375px">Open Trades</span>
      <span style="left:520px">Profit</span><span style="left:610px">Active Trading</span><span style="left:780px">Deposit</span><span style="left:970px">More settings</span>
    </div>
    <div class="dash-row">
      <span style="left:10px;top:12px;font-weight:700;color:#c8961e">Crestline Option</span>
      <span style="left:200px;top:12px">£8,549.50</span><span style="left:395px;top:12px">£0</span><span style="left:505px;top:12px">£ 2,151.00</span>
      <span class="toggle" style="left:635px;top:13px"></span>
      <span style="left:760px;top:10px;width:92px;height:26px;background:var(--orange);color:#fff;font-size:13px;text-align:center;line-height:26px;border-radius:2px">Deposit</span>
      <span style="left:895px;top:14px;width:30px;height:20px;background:#e8643a;border-radius:3px"></span>
      <span style="left:1000px;top:8px;font-size:20px">⌃</span>
    </div>
    <div class="dash-lower">
      <span class="label" style="left:80px;top:12px">Trade Options</span>
      <span class="label" style="left:690px;top:12px">Assets</span>
      <span class="opt" style="left:10px;top:62px">Daily Stop Loss</span>
      <span class="opt" style="left:140px;top:56px;width:80px;height:28px;background:#fff;border:1px solid #ccc;padding:5px 8px">5000</span>
      <span class="opt" style="left:10px;top:102px">Max Daily Trades</span>
      <span class="opt" style="left:140px;top:96px;width:80px;height:28px;background:#fff;border:1px solid #ccc;padding:5px 8px">100</span>
      <span class="toggle abs" style="left:255px;top:58px"></span><span class="opt" style="left:330px;top:60px">Nordvale</span>
      <span class="toggle abs" style="left:255px;top:98px"></span><span class="opt" style="left:330px;top:100px">Arcwell</span>
      <span class="toggle abs" style="left:535px;top:58px"></span><span class="opt" style="left:610px;top:60px">Lumisoft</span>
      <span class="toggle abs" style="left:535px;top:98px"></span><span class="opt" style="left:610px;top:100px">Corevia Co</span>
      <span class="toggle abs" style="left:815px;top:58px"></span><span class="opt" style="left:890px;top:60px">Fizzbrook</span>
      <span class="toggle abs" style="left:815px;top:98px"></span><span class="opt" style="left:890px;top:100px">Halden Foods</span>
      <div class="fade"></div>
    </div>
  </div>
</section>

<section class="contact">
  <h2 class="abs h center">CONTACT</h2>
  <div class="abs input" style="left:68px;top:125px">Name</div>
  <div class="abs input" style="left:68px;top:202px">Email</div>
  <div class="abs input" style="left:68px;top:281px">Phone</div>
  <div class="abs input" style="left:68px;top:360px">Subject</div>
  <div class="abs textarea">Type Your Message</div>
  <div class="abs btn-msg">Message</div>
</section>

<footer class="footer">
  <h4 style="left:55px;top:45px">Affiliate Program</h4>
  <p class="abs legal">Information on QuillmarshTrades.com should not be seen as a recommendation to trade binary options. QuillmarshTrades.com is a free software that enables you to receive free binary signals from third parties. The site is not licensed or authorized to provide advice on investing and related matters. Information on the website is not, nor should it be seen as investment advice. Clients without sufficient knowledge should seek individual advice from an authorized source. Binary options trading entails significant risk and there is a chance that clients lose their investments. Past performance is not a guarantee of future returns.<br><br>Our software is independent of the brokers featured herein. Before trading with any of the brokers, clients should make sure they understand the risks involved. We recommend choosing an EU regulated broker for citizens residing within the EU.</p>
  <h4 style="left:680px;top:45px">Quick Links</h4>
  <ul class="abs links"><li>Home</li><li>About</li><li>FAQ</li><li>Guides</li><li>Contact</li></ul>
  <h4 style="left:970px;top:45px">Follow us</h4>
  <span class="abs social" style="left:972px;background:#3b5998"></span>
  <span class="abs social" style="left:1014px;background:#1da1f2"></span>
  <span class="abs social" style="left:1056px;background:#dd4b39"></span>
  <span class="abs social" style="left:1098px;background:#0077b5"></span>
</footer>
<div class="abs copy" style="left:0;width:1200px">© Copyrighted All rights reserved 2017</div>

</body>
</html>
```